Design website home page for pathology consulting company

Starting a new consulting company with anatomic pathologists focused on expert diagnosis and second opinions on difficult pathology cases. In the near future we will be incorporating next generation diagnostics for rare diseases of childhood into the business. These include discovery and testing of DNA for mutations.

The company is formed around one of the best known pathologists in the world named Marcus "Buddy" Halvorsen. The name of the company is "BuddyScope"

We had a logo design by Sketchfold - it is great. I will attach file as soon as I have it (contest ending today). Our company is medical, uses microscopes, DNA, probably will focus on childhood diseases but not solely on childhood diseases. we're not particularly conservative, but the customers we want to appeal to include older practicing pathologists as well as patients (sometimes parents) looking for second opinions.

Think a group of expert doctors diagnosing disease through the microscope and through DNA technology, ages ranging from 35-75 all trained by the best pathologist in the world - "Buddy"

We receive glass slides from diseases from patients all over the world from docs who need an expert to tell them what is the diagnosis. So "path to the diagnosis" is also part of the company marketing message.

We want the website design to describe our company but be very simple to find what one is looking for as we will use it as the launch page to:
1) order services
2) check results/reports
3) set up new account
4) speak with one of the pathologists
5) see our test menu
6) access our educational material/webinars

Update - looking for home page design and then finalists will ask for second page design to keep with theme - ok?

Reason: realized this project isn't web design but web home page design - thanks

Reason: Holidays for some in next two weeks

Reason: Hot discussion among collaborators for a few of the submissions. Will provide detail individually this weekend. Thanks so much for all the submissions!

Target Market(s)

Referring pathologists, physicians who want second opinions on pathology disease diagnosis, patients who have had biopsies (either patients themselves or parents of patients), generally high education level

Industry/Entity Type

Marketing

Requirements
Must have
• BuddyScope
Next Generation Pathology Consultants

```html
<!DOCTYPE html>
<html lang="en">
<head>
<meta charset="utf-8">
<title>BuddyScope — Next Generation Pathology Consultants</title>
<link rel="stylesheet" href="https://fonts.googleapis.com/css2?family=PT+Sans:wght@400;700&family=Arimo:wght@400&display=swap">
<style>
  :root {
    --ink-black: #000000;
    --brand-blue: #0a69ad;
    --brand-blue-bright: #1e7fd0;
    --tile-blue: #0b67ac;
    --panel-grey: #e1e1e1;
    --rule-grey: #cfcfcf;
    --text-dark: #111111;
    --text-body: #666666;
    --text-light: #d9d9d9;
    --white: #ffffff;
    --input-grey: #e6e6e6;
    --dot-grey: #dcdcdc;
    --hero-dark: #06080b;
    --hero-mid: #1b2129;
  }
  * { box-sizing: border-box; margin: 0; padding: 0; }
  html, body { width: 1200px; height: 1000px; overflow: hidden; }
  body { position: relative; background: var(--panel-grey); font-family: "PT Sans", "Trebuchet MS", sans-serif; color: var(--text-dark); }
  a { color: inherit; }

  /* Hero */
  .hero { position: absolute; left: 0; top: 0; width: 1200px; height: 475px; background: var(--ink-black); }
  .brand { position: absolute; left: 168px; top: 56px; display: flex; flex-direction: column; }
  .brand-mark { width: 34px; height: 34px; border-radius: 50%; background: var(--brand-blue); margin: 0 0 6px 62px; }
  .brand-name { font-weight: 400; font-size: 27px; letter-spacing: 0.5px; color: var(--brand-blue); line-height: 1; text-transform: uppercase; }
  .brand-tagline { font-size: 9.5px; color: var(--text-light); margin-top: 3px; }

  .main-nav { position: absolute; left: 560px; top: 27px; display: flex; gap: 8px; }
  .nav-tile { position: relative; width: 78px; height: 105px; background: var(--tile-blue); display: flex; flex-direction: column; align-items: center; text-decoration: none; font-family: "Arimo", Arial, sans-serif; font-size: 13px; color: var(--white); }
  .nav-tile.is-active::before { content: ""; position: absolute; left: 0; top: -4px; width: 100%; height: 4px; background: #b8b8b8; }
  .nav-tile.is-active { color: var(--ink-black); }
  .nav-tile svg { margin-top: 18px; width: 48px; height: 48px; }
  .nav-tile span { margin-top: 7px; }

  .hero-visual { position: absolute; left: 595px; top: 132px; width: 385px; height: 333px;
    background: linear-gradient(90deg, var(--hero-dark) 0%, var(--hero-mid) 60%, var(--hero-dark) 100%); }

  .hero-copy { position: absolute; left: 170px; top: 210px; width: 460px; }
  .hero-kicker { font-family: "Arimo", Arial, sans-serif; font-size: 17px; color: var(--white); }
  .hero-title { font-weight: 400; font-size: 39px; letter-spacing: 1px; color: var(--brand-blue); text-transform: uppercase; line-height: 1; margin-top: 4px; }
  .hero-text { font-family: "Arimo", Arial, sans-serif; font-size: 12.5px; line-height: 20.5px; color: var(--text-light); margin-top: 20px; }
  .hero-more { display: block; font-size: 10px; color: var(--brand-blue); text-decoration: none; margin-top: 14px; }

  .slider-dots { position: absolute; left: 556px; top: 437px; display: flex; gap: 6px; }
  .slider-dots i { width: 11px; height: 10px; background: var(--dot-grey); }
  .slider-dots i.is-current { background: var(--brand-blue); }

  /* Utility band */
  .utility-band { position: absolute; left: 0; top: 475px; width: 1200px; height: 63px; background: var(--brand-blue); color: var(--white); }
  .search-label { position: absolute; left: 170px; top: 22px; font-size: 17px; letter-spacing: 0.3px; text-transform: uppercase; }
  .search-field { position: absolute; left: 325px; top: 16px; width: 235px; height: 31px; background: var(--input-grey); }
  .search-button { position: absolute; left: 562px; top: 16px; width: 31px; height: 31px; background: #0a5e9c; }
  .contact-icon { position: absolute; left: 662px; top: 16px; }
  .contact-number { position: absolute; left: 719px; top: 11px; font-size: 20px; }
  .contact-link { position: absolute; left: 720px; top: 38px; font-size: 10px; }

  /* Content */
  .column { position: absolute; top: 586px; }
  .column-news { left: 170px; width: 423px; }
  .column-cases { left: 662px; width: 318px; }
  .section-title { font-weight: 400; font-size: 17px; color: var(--text-dark); }
  .view-all { display: block; font-size: 9.5px; color: var(--brand-blue); margin-top: 1px; }

  .news-item { position: relative; padding-bottom: 11px; }
  .news-item + .news-item { border-top: 1px solid var(--rule-grey); padding-top: 9px; }
  .news-list { margin-top: 16px; }
  .news-title { font-weight: 400; font-size: 13px; color: var(--brand-blue); line-height: 18px; }
  .news-date { position: absolute; right: 0; top: 0; width: 77px; height: 22px; background: var(--brand-blue); color: var(--white); font-size: 7.5px; text-align: center; line-height: 22px; }
  .news-item + .news-item .news-date { top: 9px; }
  .news-text, .case-text { font-size: 9.5px; line-height: 11.5px; color: var(--text-body); margin-top: 6px; }

  .case-item { position: absolute; left: 0; display: flex; gap: 11px; }
  .case-thumb { width: 86px; height: 86px; background: var(--white); padding: 9px 8px; flex: none; }
  .case-thumb div { width: 100%; height: 100%; background: linear-gradient(135deg, #a7d7f3 0%, #4aa3d9 55%, #2a4fa6 100%); }
  .case-title { font-weight: 400; font-size: 13px; color: var(--brand-blue); line-height: 18px; }
  .case-link { display: block; font-size: 9.5px; color: var(--brand-blue); margin-top: 14px; }

  /* Footer */
  .site-footer { position: absolute; left: 0; top: 910px; width: 1200px; height: 90px; background: var(--ink-black); }
  .follow-box { position: absolute; left: 170px; top: -5px; width: 145px; height: 95px; background: var(--brand-blue); clip-path: polygon(0 0, 141px 0, 145px 5px, 145px 100%, 0 100%); }
  .follow-title { position: absolute; left: 17px; top: 26px; font-family: "Arimo", Arial, sans-serif; font-size: 12px; color: var(--white); }
  .social-links { position: absolute; left: 17px; top: 53px; display: flex; gap: 5px; }
  .social-links span { width: 28px; height: 28px; border-radius: 50%; background: var(--brand-blue-bright); }
  .social-links span:first-child { background: #2b2b2b; }
  .footer-nav { position: absolute; left: 416px; top: 46px; font-size: 9.5px; color: var(--white); white-space: nowrap; }
  .footer-nav a { text-decoration: none; }
  .footer-nav a.is-active { color: var(--brand-blue-bright); }
  .footer-nav .sep { margin: 0 6px; }
  .footer-brand { position: absolute; right: 222px; top: 10px; text-align: right; }
  .footer-brand-mark { width: 22px; height: 22px; border-radius: 50%; background: var(--brand-blue); margin-left: auto; margin-right: 20px; }
  .footer-brand-name { font-size: 14px; color: var(--brand-blue); text-transform: uppercase; line-height: 1; margin-top: 6px; }
  .footer-brand-tag { font-size: 4.5px; color: var(--text-light); }
  .footer-copy { position: absolute; right: 222px; top: 68px; font-size: 7.5px; color: var(--text-light); text-align: right; }
</style>
</head>
<body>

<header class="hero">
  <div class="brand">
    <span class="brand-mark"></span>
    <span class="brand-name">BuddyScope</span>
    <span class="brand-tagline">Next Generation Pathology Consultants</span>
  </div>

  <nav class="main-nav">
    <a class="nav-tile is-active" href="#">
      <svg viewBox="0 0 48 48"><circle cx="24" cy="24" r="22" fill="#000"/><circle cx="25.5" cy="13" r="3" fill="#1e7fd0"/><path d="M20 20h8l-4 16h4l-1 3h-8l4-16h-4z" fill="#1e7fd0"/></svg>
      <span>About Us</span>
    </a>
    <a class="nav-tile" href="#">
      <svg viewBox="0 0 48 48" fill="#d8d8d8"><rect x="20" y="3" width="7" height="20" rx="1" transform="rotate(-15 23 13)"/><path d="M28 18a12 12 0 0 1-2 20h8a14 14 0 0 0-2-22z"/><rect x="14" y="26" width="14" height="3"/><rect x="10" y="38" width="28" height="5" rx="1"/><rect x="18" y="29" width="5" height="9"/></svg>
      <span>Our Team</span>
    </a>
    <a class="nav-tile" href="#">
      <svg viewBox="0 0 48 48" fill="none" stroke="#d8d8d8" stroke-width="2.5"><path d="M10 4h20l8 8v32H10z"/><path d="M30 4v8h8"/><path d="M15 20l3 3 5-6M15 32l3 3 5-6M26 21h8M26 33h8"/></svg>
      <span>Reports</span>
    </a>
    <a class="nav-tile" href="#">
      <svg viewBox="0 0 48 48"><g fill="#d8d8d8"><circle cx="24" cy="24" r="15"/><g id="teeth"><rect x="20" y="2" width="8" height="9"/><rect x="20" y="37" width="8" height="9"/></g><use href="#teeth" transform="rotate(45 24 24)"/><use href="#teeth" transform="rotate(90 24 24)"/><use href="#teeth" transform="rotate(135 24 24)"/></g><circle cx="24" cy="24" r="6" fill="#0b67ac"/></svg>
      <span>Services</span>
    </a>
    <a class="nav-tile" href="#">
      <svg viewBox="0 0 48 48"><circle cx="24" cy="24" r="21" fill="none" stroke="#d8d8d8" stroke-width="2.5"/><path d="M17 13l5 0 2 6-3 2c1 3 4 6 7 7l2-3 6 2v5c-8 1-20-9-19-19z" fill="#d8d8d8"/></svg>
      <span>Contact Us</span>
    </a>
  </nav>

  <div class="hero-visual" role="img" aria-label="Photograph of laboratory microscope equipment"></div>

  <section class="hero-copy">
    <p class="hero-kicker">Welcome To</p>
    <h1 class="hero-title">BuddyScope</h1>
    <p class="hero-text">Lorem Ipsum is simply dummy text of the printing and typesetting industry. Lorem Ipsum has been the industry's standard dummy text ever since the 1500s, when an unknown printer took a galley of type and scrambled it to make a type specimen book.</p>
    <a class="hero-more" href="#">read more about us....</a>
  </section>

  <div class="slider-dots"><i class="is-current"></i><i></i><i></i><i></i></div>
</header>

<section class="utility-band">
  <span class="search-label">Search our site</span>
  <div class="search-field"></div>
  <div class="search-button">
    <svg width="31" height="31" viewBox="0 0 31 31"><circle cx="17" cy="13" r="6" fill="#a9c6de" stroke="#e6e6e6" stroke-width="2"/><path d="M12.5 17.5l-5 5" stroke="#e6e6e6" stroke-width="3" stroke-linecap="round"/></svg>
  </div>
  <svg class="contact-icon" width="32" height="32" viewBox="0 0 32 32"><circle cx="16" cy="16" r="14.5" fill="none" stroke="#fff" stroke-width="2"/><path d="M11 8.5h3.5l1.3 4-2 1.4c.8 2 2.5 3.8 4.5 4.6l1.4-2 4 1.3v3.5c-6 .6-13.5-6.6-12.7-12.8z" fill="#fff"/></svg>
  <span class="contact-number">555 014 27390</span>
  <a class="contact-link" href="#">Click Here to Contact Us</a>
</section>

<main>
  <section class="column column-news">
    <h2 class="section-title">Latest News &amp; Announcement</h2>
    <a class="view-all" href="#">View All</a>
    <div class="news-list">
      <article class="news-item">
        <h3 class="news-title">Lorem Ipsum is simply dummy text</h3>
        <span class="news-date">October 14, 2013</span>
        <p class="news-text">Lorem Ipsum is simply dummy text of the printing and typesetting industry. Lorem Ipsum has been the industry's standard dummy text ever since</p>
      </article>
      <article class="news-item">
        <h3 class="news-title">Lorem Ipsum is simply dummy text</h3>
        <span class="news-date">October 14, 2013</span>
        <p class="news-text">Lorem Ipsum is simply dummy text of the printing and typesetting industry. Lorem Ipsum has been the industry's standard dummy text ever since</p>
      </article>
    </div>
  </section>

  <section class="column column-cases">
    <h2 class="section-title">Case In Focus</h2>
    <a class="view-all" href="#">View All</a>
    <article class="case-item" style="top:55px">
      <div class="case-thumb"><div role="img" aria-label="Illustration of a molecular structure in blue and purple"></div></div>
      <div>
        <h3 class="case-title">Lorem Ipsum is simply</h3>
        <p class="case-text">Lorem Ipsum is simply dummy text of the printing and typesetting industry. Lorem Ipsum has been the industry's standard dummy text ever since</p>
        <a class="case-link" href="#">View Detail</a>
      </div>
    </article>
    <article class="case-item" style="top:171px">
      <div class="case-thumb"><div role="img" aria-label="Illustration of a molecular structure in blue and purple"></div></div>
      <div>
        <h3 class="case-title">Lorem Ipsum is simply</h3>
        <p class="case-text">Lorem Ipsum is simply dummy text of the printing and typesetting industry. Lorem Ipsum has been the industry's standard dummy text ever since</p>
        <a class="case-link" href="#">View Detail</a>
      </div>
    </article>
  </section>
</main>

<footer class="site-footer">
  <div class="follow-box">
    <span class="follow-title">Follow Us</span>
    <div class="social-links">
      <span role="img" aria-label="Social network link"></span>
      <span role="img" aria-label="Social network link"></span>
      <span role="img" aria-label="Social network link"></span>
    </div>
  </div>
  <nav class="footer-nav">
    <a class="is-active" href="#">About Us</a><span class="sep">|</span><a href="#">Our Team</a><span class="sep">|</span><a href="#">Report</a><span class="sep">|</span><a href="#">Services</a><span class="sep">|</span><a href="#">Contact Us</a><span class="sep">|</span><a href="#">Privacy</a><span class="sep">|</span><a href="#">Terms</a>
  </nav>
  <div class="footer-brand">
    <div class="footer-brand-mark"></div>
    <div class="footer-brand-name">BuddyScope</div>
    <div class="footer-brand-tag">Next Generation Pathology Consultants</div>
  </div>
  <p class="footer-copy">All Right Reserved Copyright BuddyScope.</p>
</footer>

</body>
</html>
```